Business cards and Stationary for engineering design firm
Brask Industrial Advisory
Business cards and Stationary for engineering design firm - Engineering
Creative Brief
Professional
Dorian Pell
President
42 N 9th St Marlow, PA 17362
Dorian@BraskIndAdvisory.example
www.BraskIndAdvisory.example
We are looking for modern and professional looking business cards for an engineering firm that specializes in the electric utility industry. Subtle touches like abstract poles and wires on the business cards are welcomed. Use your imagination and have fun!
We are up for anything. Maybe just the company logo and the website address for the back.

```html
<!DOCTYPE html>
<html lang="en">
<head>
<meta charset="utf-8">
<title>Brask Industrial Advisory — Stationery</title>
<link href="https://fonts.googleapis.com/css2?family=Cinzel:wght@500&family=Montserrat:wght@400;500&display=swap" rel="stylesheet">
<style>
  :root {
    --bg: #e8e9eb;
    --paper: #ffffff;
    --navy: #2d4a78;
    --navy-deep: #1d3461;
    --ink: #111111;
    --grey: #8a8f98;
    --text: #555a62;
  }
  * { box-sizing: border-box; margin: 0; padding: 0; }
  html, body { width: 1200px; height: 937px; overflow: hidden; background: var(--bg); }
  body { position: relative; font-family: "Montserrat", sans-serif; color: var(--text); }

  .sheet { position: absolute; background: var(--paper); box-shadow: 0 2px 6px rgba(0,0,0,.18); overflow: hidden; }
  .wave { position: absolute; left: 0; bottom: 0; width: 100%; display: block; }

  .brand { position: absolute; display: flex; flex-direction: column; align-items: center; }
  .brand-mark { border-radius: 50%; background: var(--navy); }
  .brand-name { font-family: "Cinzel", serif; font-weight: 500; color: var(--navy-deep); white-space: nowrap; line-height: 1.1; text-align: center; }
  .brand-tagline { font-family: "Montserrat", sans-serif; color: var(--navy); letter-spacing: .14em; white-space: nowrap; text-transform: uppercase; }

  /* Letterhead */
  .letterhead { left: 182px; top: 68px; width: 388px; height: 542px; }
  .letterhead .brand { left: 28px; top: 24px; }
  .letterhead .brand-mark { width: 36px; height: 36px; margin-bottom: 6px; }
  .letterhead .brand-name { font-size: 15px; }
  .letterhead .brand-tagline { font-size: 5.5px; margin-top: 3px; }
  .sender { position: absolute; right: 24px; top: 30px; text-align: right; font-size: 5.5px; line-height: 1.6; color: var(--text); }
  .letter-body { position: absolute; left: 30px; top: 118px; width: 320px; font-size: 5.5px; line-height: 1.7; }
  .letter-body p { margin-bottom: 9px; }
  .signoff { margin-top: 26px; }

  /* Folder */
  .folder { left: 635px; top: 43px; width: 458px; height: 569px; }
  .folder .brand { left: 0; right: 0; top: 210px; }
  .folder .brand-mark { width: 80px; height: 80px; margin-bottom: 12px; }
  .folder .brand-name { font-size: 27px; }
  .folder .brand-tagline { font-size: 10px; margin-top: 6px; }

  /* Cards */
  .card { left: 46px; width: 159px; }
  .card-front { top: 665px; height: 95px; }
  .card-back { top: 785px; height: 98px; }
  .card-front .brand { left: 8px; top: 12px; }
  .card-front .brand-mark { width: 14px; height: 14px; margin-bottom: 3px; }
  .card-front .brand-name { font-size: 6px; }
  .card-front .brand-tagline { font-size: 2.4px; margin-top: 1px; }
  .card-contact { position: absolute; right: 8px; top: 14px; text-align: right; font-size: 3.6px; line-height: 1.6; }
  .card-contact .person { font-weight: 500; color: var(--navy-deep); font-size: 4.4px; }
  .card-back .brand { left: 0; right: 0; top: 18px; }
  .card-back .brand-mark { width: 18px; height: 18px; margin-bottom: 4px; }
  .card-back .brand-name { font-size: 8px; }
  .card-back .brand-tagline { font-size: 3px; margin-top: 2px; }

  /* Envelopes */
  .envelope-front { left: 266px; top: 670px; width: 432px; height: 213px; }
  .envelope-front .brand { left: 20px; top: 16px; }
  .envelope-front .brand-mark { width: 22px; height: 22px; margin-bottom: 4px; }
  .envelope-front .brand-name { font-size: 10px; }
  .envelope-front .brand-tagline { font-size: 3.8px; margin-top: 2px; }
  .envelope-back { left: 737px; top: 670px; width: 356px; height: 210px; }
  .flap { position: absolute; left: 0; top: 0; width: 100%; }
  .flap-web { position: absolute; left: 0; right: 0; top: 26px; text-align: center; color: #fff; font-size: 10px; letter-spacing: .12em; }
</style>
</head>
<body>

<!-- Letterhead -->
<section class="sheet letterhead">
  <div class="brand">
    <span class="brand-mark"></span>
    <span class="brand-name">Brask Industrial<br>Advisory</span>
    <span class="brand-tagline">Electric Utility Design Solutions</span>
  </div>
  <address class="sender" style="font-style:normal">
    42 N 9th St Marlow, PA 17362<br>
    Dorian@BraskIndAdvisory.example<br>
    www.BraskIndAdvisory.example
  </address>
  <div class="letter-body">
    <p>June 4, 2024</p>
    <p>Recipient Name<br>Company Address</p>
    <p>Thank you for meeting with our team last week. We are pleased to share the outline of our proposed distribution design work and the schedule we discussed for the coming quarter.</p>
    <p>Our engineers will review pole loading, clearances and line routing before submitting final drawings for your approval.</p>
    <p>Please contact us with any questions. We look forward to working with you.</p>
    <p>Sincerely,</p>
    <p class="signoff">Dorian Pell<br>President</p>
  </div>
  <svg class="wave" viewBox="0 0 400 60" preserveAspectRatio="none" height="40">
    <path d="M0,30 C110,8 240,46 400,14 L400,19 C240,52 110,15 0,36 Z" fill="var(--ink)"/>
    <path d="M0,38 C110,20 240,56 400,24 L400,60 L0,60 Z" fill="var(--navy)"/>
  </svg>
</section>

<!-- Folder -->
<section class="sheet folder">
  <div class="brand">
    <span class="brand-mark"></span>
    <span class="brand-name">Brask Industrial<br>Advisory</span>
    <span class="brand-tagline">Electric Utility Design Solutions</span>
  </div>
  <svg class="wave" viewBox="0 0 400 60" preserveAspectRatio="none" height="50">
    <path d="M0,30 C110,8 240,46 400,14 L400,19 C240,52 110,15 0,36 Z" fill="var(--ink)"/>
    <path d="M0,38 C110,20 240,56 400,24 L400,60 L0,60 Z" fill="var(--navy)"/>
  </svg>
</section>

<!-- Business card front -->
<section class="sheet card card-front">
  <div class="brand">
    <span class="brand-mark"></span>
    <span class="brand-name">Brask Industrial<br>Advisory</span>
    <span class="brand-tagline">Electric Utility Design Solutions</span>
  </div>
  <div class="card-contact">
    <div class="person">Dorian Pell</div>
    <div>President</div>
    <div>42 N 9th St Marlow, PA 17362</div>
    <div>Dorian@BraskIndAdvisory.example</div>
    <div>www.BraskIndAdvisory.example</div>
  </div>
  <svg class="wave" viewBox="0 0 400 60" preserveAspectRatio="none" height="22">
    <path d="M0,30 C110,8 240,46 400,14 L400,19 C240,52 110,15 0,36 Z" fill="var(--ink)"/>
    <path d="M0,38 C110,20 240,56 400,24 L400,60 L0,60 Z" fill="var(--navy)"/>
  </svg>
</section>

<!-- Business card back -->
<section class="sheet card card-back">
  <div class="brand">
    <span class="brand-mark"></span>
    <span class="brand-name">Brask Industrial<br>Advisory</span>
    <span class="brand-tagline">Electric Utility Design Solutions</span>
  </div>
</section>

<!-- Envelope front -->
<section class="sheet envelope-front">
  <div class="brand">
    <span class="brand-mark"></span>
    <span class="brand-name">Brask Industrial<br>Advisory</span>
    <span class="brand-tagline">Electric Utility Design Solutions</span>
  </div>
  <svg class="wave" viewBox="0 0 400 60" preserveAspectRatio="none" height="44">
    <path d="M0,30 C110,8 240,46 400,14 L400,19 C240,52 110,15 0,36 Z" fill="var(--ink)"/>
    <path d="M0,38 C110,20 240,56 400,24 L400,60 L0,60 Z" fill="var(--navy)"/>
  </svg>
</section>

<!-- Envelope back -->
<section class="sheet envelope-back">
  <svg class="flap" viewBox="0 0 356 110" preserveAspectRatio="none" height="110">
    <path d="M0,0 L356,0 L356,6 C300,40 240,92 178,104 C116,92 56,40 0,6 Z" fill="var(--navy)"/>
  </svg>
  <div class="flap-web">www.BraskIndAdvisory.example</div>
</section>

</body>
</html>
```